Wordpress Design Project (Varnet)

We need a wordpress design for an established auction and real estate company based in Pennsylvania. The winning design will incorporate a professional layout with and company logo in a very simple and clean layout.

Industry/Entity Type

Real Estate

Requirements
Must have
• Navigation:
1) Home; 2) Auctions; 3) Appraisals; 4) Real Estate; 5) FAQ; 6) About Us; 7) Contact Us.

Site will have overall layout of https://www.plimtova.com/featured/regions/the-northeast. Home page will have logo and navigation at top. The navigation bar will also have social media icons (facebook, Google+, RSS, twitter) inside it. There will be text in the content area - use lorem ipsum. The image attached will be used below text (auctions.jpg) . Footer will have smaller company loogo, the attached affiliation logos and social media icons.

Logo attached. Color scheme will be black, gray, and red as accent color.
Nice to have
• navigation will have dropdowns, nice to have one represented - under auctions 'All Auctions' will be dropdown.

```html
<!DOCTYPE html>
<html lang="en">
<head>
<meta charset="utf-8">
<title>Varnet Auctioneers &amp; Appraisers</title>
<link href="https://fonts.googleapis.com/css2?family=Raleway:wght@400;500;600;700&display=swap" rel="stylesheet">
<style>
:root{
  --red:#d9261c;
  --ink:#333;
  --muted:#777;
  --page:#efefef;
  --card:#fff;
  --footer:#000;
  --line:#dcdcdc;
  --social:#888;
}
*{box-sizing:border-box;margin:0;padding:0}
html,body{width:727px;height:1200px;overflow:hidden}
body{background:var(--page);font-family:"Raleway",sans-serif;color:var(--ink);position:relative}
.abs{position:absolute}
.brand{left:76px;top:48px}
.brand-name{font-size:30px;font-weight:600;color:#111;letter-spacing:.5px;line-height:32px}
.search{left:487px;top:32px;width:164px;height:18px;display:flex}
.search input{flex:1;border:1px solid #e2e2e2;background:#fff;height:18px}
.search button{width:37px;background:var(--red);color:#fff;border:0;font:500 7px "Raleway",sans-serif}
.nav{top:69px;left:0;font-size:10px;color:#444}
.nav a{color:inherit;text-decoration:none;position:absolute;white-space:nowrap}
.hero{left:0;top:105px;width:727px;height:232px;background:linear-gradient(180deg,#7fb2dc 0%,#a9664a 38%,#6f9a3c 62%,#4fa7c9 100%)}
.arrow{width:28px;height:28px;border-radius:50%;background:rgba(255,255,255,.85);display:flex;align-items:center;justify-content:center}
.badge{left:464px;top:202px;width:115px;height:38px;background:var(--red);color:#fff;font-weight:700;font-size:13px;line-height:15px;padding:5px 0 0 34px;border-radius:3px}
.badge span{display:block;font-weight:500}
.welcome{top:346px;width:727px;text-align:center;color:var(--red);font-size:14px;font-weight:500}
.divider{top:367px;left:0;width:727px;height:1px;background:var(--line)}
.intro{top:372px;left:76px;width:575px;text-align:center;font-size:8.4px;line-height:14.5px;letter-spacing:.3px;color:var(--muted)}
.card{width:261px;height:154px;background:var(--card);box-shadow:0 0 2px rgba(0,0,0,.08)}
.card .photo{position:absolute;left:8px;top:7px;width:246px;height:94px}
.card .title{position:absolute;left:8px;top:109px;font-size:8.5px;color:#333;font-weight:500}
.card .place{position:absolute;right:8px;top:109px;font-size:7px;color:#333;display:flex;align-items:center;gap:3px}
.card .sub{position:absolute;left:8px;top:124px;font-size:7px;color:var(--muted)}
.card .date{position:absolute;left:8px;top:139px;font-size:7px;color:var(--red)}
.notice{top:975px;width:727px;text-align:center;font-size:8.5px;line-height:14.5px;color:var(--muted)}
.signup{left:189px;top:1020px;display:flex;gap:2px}
.signup input{width:281px;height:20px;border:0;background:#fff;padding-left:8px;font:8px "Raleway",sans-serif;color:#888}
.signup button{width:67px;height:20px;border:0;background:var(--red);color:#fff;font:700 8.5px "Raleway",sans-serif}
.aff-title{top:1053px;width:727px;text-align:center;font-size:11.5px;font-weight:400;color:#333}
.footer{left:0;top:1136px;width:727px;height:64px;background:var(--footer);color:#fff}
.footer-nav{left:76px;top:13px;font-size:8.5px}
.footer-legal{left:76px;top:36px;font-size:7px}
.social{position:absolute;top:24px;width:20px;height:20px;border-radius:50%;background:var(--social)}
</style>
</head>
<body>
<header>
  <div class="abs brand"><span class="brand-name">Varnet</span></div>
  <form class="abs search"><input type="text" aria-label="Search"><button type="button">SEARCH</button></form>
  <nav class="abs nav">
    <a style="left:269px">Home</a><a style="left:312px">Auctions</a><a style="left:369px">Appraisals</a><a style="left:433px">Real Estate</a><a style="left:502px">FAQ</a><a style="left:539px">About Us</a><a style="left:598px">Contact Us</a>
  </nav>
</header>

<section class="abs hero" role="img" aria-label="Resort house with lawn, palm trees and pool, with an auction gavel"></section>
<div class="abs arrow" style="left:44px;top:200px"><svg width="12" height="12" viewBox="0 0 12 12"><path d="M8 1 3 6l5 5" fill="none" stroke="#555" stroke-width="2"/></svg></div>
<div class="abs arrow" style="left:655px;top:200px"><svg width="12" height="12" viewBox="0 0 12 12"><path d="M4 1l5 5-5 5" fill="none" stroke="#555" stroke-width="2"/></svg></div>
<div class="abs badge">AUCTION<span>FOR SALE</span></div>

<h1 class="abs welcome">Welcome to Varnet</h1>
<div class="abs divider"></div>
<p class="abs intro">Lorem Ipsum is simply dummy text of the printing and typesetting industry. Lorem Ipsum has been the industry's standard dummy text ever since the 1500s, when an unknown printer took a galley of type and scrambled it to make a type specimen book. It has survived not only five centuries, but also the leap into electronic typesetting, remaining essentially unchanged. It was popularised in the 1960s with the release of Lettrafix sheets containing Lorem Ipsum passages, and more recently with desktop publishing software like Orvel PageSetter including versions of Lorem Ipsum.</p>

<main>
  <article class="abs card" style="left:100px;top:467px"><div class="photo" role="img" aria-label="Wooden cabinets with lot tags" style="background:linear-gradient(90deg,#c79a6e,#6b2a1c 50%,#8a4a32)"></div><div class="title">At vero eos et accusamus</div><div class="place"><svg width="8" height="11" viewBox="0 0 8 11"><path d="M4 0a4 4 0 0 1 4 4c0 3-4 7-4 7S0 7 0 4a4 4 0 0 1 4-4z" fill="#d9261c"/><circle cx="4" cy="4" r="1.5" fill="#fff"/></svg>Brooklandville ,MD</div><div class="sub">Veritatis et quasi architecto</div><div class="date">10-08-2013</div></article>
  <article class="abs card" style="left:366px;top:467px"><div class="photo" role="img" aria-label="Rolled carpets with lot tags" style="background:linear-gradient(90deg,#8f8a80,#b8b2a6 50%,#7d8590)"></div><div class="title">At vero eos et accusamus</div><div class="place"><svg width="8" height="11" viewBox="0 0 8 11"><path d="M4 0a4 4 0 0 1 4 4c0 3-4 7-4 7S0 7 0 4a4 4 0 0 1 4-4z" fill="#d9261c"/><circle cx="4" cy="4" r="1.5" fill="#fff"/></svg>Brooklandville ,MD</div><div class="sub">Veritatis et quasi architecto</div><div class="date">10-08-2013</div></article>
  <article class="abs card" style="left:100px;top:633px"><div class="photo" role="img" aria-label="Row of white interior doors" style="background:linear-gradient(90deg,#e8e6e0,#f4f2ec 60%,#b8956a)"></div><div class="title">At vero eos et accusamus</div><div class="place"><svg width="8" height="11" viewBox="0 0 8 11"><path d="M4 0a4 4 0 0 1 4 4c0 3-4 7-4 7S0 7 0 4a4 4 0 0 1 4-4z" fill="#d9261c"/><circle cx="4" cy="4" r="1.5" fill="#fff"/></svg>Brooklandville ,MD</div><div class="sub">Veritatis et quasi architecto</div><div class="date">10-08-2013</div></article>
  <article class="abs card" style="left:366px;top:633px"><div class="photo" role="img" aria-label="Vanity cabinets with granite tops" style="background:linear-gradient(180deg,#5a3a28,#2c2622 35%,#b0652e)"></div><div class="title">At vero eos et accusamus</div><div class="place"><svg width="8" height="11" viewBox="0 0 8 11"><path d="M4 0a4 4 0 0 1 4 4c0 3-4 7-4 7S0 7 0 4a4 4 0 0 1 4-4z" fill="#d9261c"/><circle cx="4" cy="4" r="1.5" fill="#fff"/></svg>Brooklandville ,MD</div><div class="sub">Veritatis et quasi architecto</div><div class="date">10-08-2013</div></article>
  <article class="abs card" style="left:100px;top:800px"><div class="photo" role="img" aria-label="Movers carrying an orange armchair by a staircase" style="background:linear-gradient(90deg,#ece9e4,#f6f4f0 50%,#e08a4a 75%,#efece8)"></div><div class="title">At vero eos et accusamus</div><div class="place"><svg width="8" height="11" viewBox="0 0 8 11"><path d="M4 0a4 4 0 0 1 4 4c0 3-4 7-4 7S0 7 0 4a4 4 0 0 1 4-4z" fill="#d9261c"/><circle cx="4" cy="4" r="1.5" fill="#fff"/></svg>Brooklandville ,MD</div><div class="sub">Veritatis et quasi architecto</div><div class="date">10-08-2013</div></article>
  <article class="abs card" style="left:366px;top:800px"><div class="photo" role="img" aria-label="Wooden kitchen with a long counter" style="background:linear-gradient(180deg,#6b4a34,#8a4a26 50%,#d8cfc0)"></div><div class="title">At vero eos et accusamus</div><div class="place"><svg width="8" height="11" viewBox="0 0 8 11"><path d="M4 0a4 4 0 0 1 4 4c0 3-4 7-4 7S0 7 0 4a4 4 0 0 1 4-4z" fill="#d9261c"/><circle cx="4" cy="4" r="1.5" fill="#fff"/></svg>Brooklandville ,MD</div><div class="sub">Veritatis et quasi architecto</div><div class="date">10-08-2013</div></article>
</main>

<p class="abs notice">This super awesome thing is not quite ready yet but I promise it will change your life.<br>Give me your email address and I'll hit you up when it's ready. Thanks.</p>
<form class="abs signup"><input type="text" value="enter your email address..." aria-label="Email"><button type="button">Submit</button></form>

<h2 class="abs aff-title">Affiliations</h2>
<svg class="abs" style="left:0;top:1078px" width="727" height="46" viewBox="0 0 727 46" aria-label="Affiliation badges">
  <g fill="none" stroke="#666" stroke-width="2">
    <rect x="165" y="5" width="30" height="34" rx="2"/>
    <ellipse cx="246" cy="22" rx="26" ry="20"/>
    <circle cx="314" cy="22" r="18"/>
    <path d="M382 4 366 40h32z"/>
    <rect x="434" y="6" width="30" height="32" rx="2"/>
    <ellipse cx="524" cy="22" rx="27" ry="16"/>
  </g>
</svg>

<footer class="abs footer">
  <div class="abs footer-nav">Home &nbsp;| &nbsp;Auctions &nbsp;| &nbsp;Appraisals &nbsp;| &nbsp;Real Estate &nbsp;| &nbsp;FAQ &nbsp;| &nbsp;About Us &nbsp;| &nbsp;Contact Us</div>
  <div class="abs footer-legal">©2013 Company Name , All Rights Reserved &nbsp;&nbsp;| &nbsp;&nbsp;Privacy Policy &nbsp;&nbsp;| &nbsp;&nbsp;Terms &amp; Conditions</div>
  <span class="social" style="left:556px"></span>
  <span class="social" style="left:580px"></span>
  <span class="social" style="left:606px"></span>
  <span class="social" style="left:632px"></span>
</footer>
</body>
</html>
```